Peaks4U LOGO + Business Card design for a Ski Tour agency

- New start-up international tour agency focused on skiing tours
- Connected with the Alps
- Targeted at Asians
- Business/Brand name: Peaks4U

```html
<!DOCTYPE html>
<html lang="en">
<head>
<meta charset="utf-8">
<title>Peaks4U Business Card</title>
<link rel="stylesheet" href="https://fonts.googleapis.com/css2?family=Roboto:wght@400;500;700&display=swap">
<style>
  :root {
    --stage: #2a2a2c;
    --card: #121213;
    --card-edge: #1c1c1e;
    --pattern-tone: #1f1f21;
    --brand-blue: #1a9fe6;
    --name-yellow: #f0e40c;
    --text-white: #f2f2f2;
    --icon-orange: #f0592a;
    --divider: #6a6a6c;
  }
  * { box-sizing: border-box; margin: 0; padding: 0; }
  html, body {
    width: 1200px; height: 1200px; overflow: hidden;
    background: var(--stage);
    font-family: "Roboto", sans-serif;
  }
  .canvas {
    position: relative; width: 1200px; height: 1200px;
  }
  .card {
    position: absolute; left: 120px; width: 960px; height: 548px;
    border-radius: 26px; overflow: hidden;
    background: var(--card);
    box-shadow: 0 18px 40px rgba(0,0,0,.45);
  }
  .card--front { top: 36px; }
  .card--back { top: 616px; }
  .card__pattern {
    position: absolute; inset: 0; width: 100%; height: 100%;
  }
  .front__brand {
    position: absolute; inset: 0;
    display: flex; align-items: center; justify-content: center; gap: 22px;
  }
  .brand-dot {
    width: 44px; height: 44px; border-radius: 50%;
    background: var(--brand-blue);
  }
  .brand-name {
    font-weight: 700; color: var(--brand-blue);
    font-size: 84px; letter-spacing: 2px;
  }
  .back__brand {
    position: absolute; left: 70px; top: 0; width: 380px; height: 100%;
    display: flex; align-items: center; justify-content: center; gap: 16px;
  }
  .back__brand .brand-name { font-size: 66px; }
  .back__brand .brand-dot { width: 36px; height: 36px; }
  .back__divider {
    position: absolute; left: 470px; top: 132px; width: 2px; height: 300px;
    background: linear-gradient(to bottom, transparent, var(--divider) 20%, var(--divider) 80%, transparent);
  }
  .contact {
    position: absolute; left: 506px; top: 148px; color: var(--text-white);
  }
  .contact__name {
    color: var(--name-yellow); font-weight: 500; font-size: 38px; line-height: 1.1;
  }
  .contact__title {
    color: var(--brand-blue); font-size: 28px; margin-top: 2px;
  }
  .contact__address {
    font-size: 22px; line-height: 1.45; margin-top: 18px;
  }
  .contact__list { list-style: none; margin-top: 16px; }
  .contact__item {
    display: flex; align-items: center; gap: 14px;
    font-size: 23px; line-height: 1.6;
  }
  .contact__icon { width: 24px; height: 24px; flex: none; }
</style>
</head>
<body>
<main class="canvas">

  <section class="card card--front" aria-label="Card front">
    <svg class="card__pattern" role="img" aria-label="Faint pattern of travel icons: planes, landmarks, luggage and vehicles" viewBox="0 0 960 548" preserveAspectRatio="none">
      <defs>
        <radialGradient id="frontTone" cx="50%" cy="45%" r="75%">
          <stop offset="0" stop-color="#161618"/>
          <stop offset="1" stop-color="#202022"/>
        </radialGradient>
      </defs>
      <rect width="960" height="548" fill="url(#frontTone)"/>
    </svg>
    <div class="front__brand">
      <span class="brand-name">Peaks4U</span>
      <span class="brand-dot"></span>
    </div>
  </section>

  <section class="card card--back" aria-label="Card back">
    <svg class="card__pattern" role="img" aria-label="Faint pattern of travel icons around the card edges" viewBox="0 0 960 548" preserveAspectRatio="none">
      <defs>
        <radialGradient id="backTone" cx="55%" cy="55%" r="70%">
          <stop offset="0" stop-color="#111112"/>
          <stop offset="1" stop-color="#1d1d1f"/>
        </radialGradient>
      </defs>
      <rect width="960" height="548" fill="url(#backTone)"/>
    </svg>

    <div class="back__brand">
      <span class="brand-dot"></span>
      <span class="brand-name">Peaks4U</span>
    </div>

    <div class="back__divider"></div>

    <div class="contact">
      <h1 class="contact__name">Marcus Whitfield</h1>
      <p class="contact__title">Managing Director</p>
      <p class="contact__address">410, 88 Harbour Street N.E<br>Banff, AB, T1L 3K7</p>
      <ul class="contact__list">
        <li class="contact__item">
          <svg class="contact__icon" viewBox="0 0 24 24" aria-hidden="true"><path fill="var(--icon-orange)" d="M6.6 10.8a15 15 0 0 0 6.6 6.6l2.2-2.2a1 1 0 0 1 1-.25 11.4 11.4 0 0 0 3.6.57 1 1 0 0 1 1 1V20a1 1 0 0 1-1 1A17 17 0 0 1 3 4a1 1 0 0 1 1-1h3.5a1 1 0 0 1 1 1c0 1.25.2 2.45.57 3.57a1 1 0 0 1-.25 1z"/></svg>
          <span>555-014-2278</span>
        </li>
        <li class="contact__item">
          <svg class="contact__icon" viewBox="0 0 24 24" aria-hidden="true" fill="none" stroke="var(--icon-orange)" stroke-width="1.8"><circle cx="12" cy="12" r="9.5"/><ellipse cx="12" cy="12" rx="4" ry="9.5"/><path d="M2.5 12h19M4 7h16M4 17h16"/></svg>
          <span>info@peaks4u.com</span>
        </li>
        <li class="contact__item">
          <svg class="contact__icon" viewBox="0 0 24 24" aria-hidden="true"><rect x="2" y="5" width="20" height="14" fill="var(--icon-orange)"/><path d="M2.5 5.5 12 13l9.5-7.5" fill="none" stroke="#fff" stroke-width="1.6"/></svg>
          <span>www.peaks4u.com</span>
        </li>
      </ul>
    </div>
  </section>

</main>
</body>
</html>
```